New Webpage for High Class Expert Witness Services Company

We are looking for a minimalist design for a webpage that just has our logo and an entry form offer to connect with one of our Liaisons.
The entry form should just ask for Name, Email, Contact Info and Description of Project.

Company Name is: The Marlow Crest Advisory Services

Number of Pages Required

1 page

```html
<!DOCTYPE html>
<html lang="en">
<head>
<meta charset="utf-8">
<title>Marlow Crest Advisory Services – Connect with a Liaison</title>
<link href="https://fonts.googleapis.com/css2?family=Cinzel:wght@400;500&family=Inter:wght@400;500&display=swap" rel="stylesheet">
<style>
:root{
  --backdrop-top:#cfcfcf;
  --backdrop-bottom:#e6e6e6;
  --ink:#0b0b0b;
  --ink-soft:#1a1a1a;
  --paper:#ffffff;
  --paper-soft:#f7f7f7;
  --line-light:#d6d6d6;
  --line-dark:#2c2c2c;
  --text-dark:#1c1c1c;
  --text-muted:#6d6d6d;
  --text-light:#f2f2f2;
  --text-dim:#9a9a9a;
  --button-light:#e9e9e9;
}
*{box-sizing:border-box;margin:0;padding:0}
html,body{width:1200px;height:862px;overflow:hidden}
body{
  background:linear-gradient(100deg,var(--backdrop-top),var(--backdrop-bottom));
  font-family:'Inter',Arial,sans-serif;
  position:relative;
}
.page{position:absolute;top:47px;width:512px;height:768px;overflow:hidden}
.page--light{left:61px;background:var(--paper)}
.page--dark{left:622px;background:radial-gradient(ellipse at 50% 35%,#1c1c1c,#050505 75%)}
.abs{position:absolute;left:0;right:0;text-align:center}

/* header */
.hero{position:absolute;top:0;left:0;right:0;height:257px;background:radial-gradient(ellipse at 50% 40%,#1d1d1d,#060606 80%)}
.brand{font-family:'Cinzel',serif;font-weight:500;color:var(--text-light);letter-spacing:1px;line-height:1.15}
.brand__name{font-size:26px}
.brand__sub{font-size:16px;letter-spacing:3px}
.brand__mark{display:inline-block;width:10px;height:10px;background:var(--text-light);margin-right:8px;vertical-align:middle}
.hero__tag{font-family:'Cinzel',serif;font-size:9.5px;letter-spacing:2.4px;color:var(--text-light)}
.btn-outline{position:absolute;border:1px solid var(--text-light);color:var(--text-light);font-size:9.5px;letter-spacing:1.4px;display:flex;align-items:center;justify-content:center}

/* features */
.features{position:absolute;top:257px;left:0;right:0;height:82px;display:flex;border-bottom:1px solid var(--line-light)}
.feature{flex:1;display:flex;flex-direction:column;align-items:center;justify-content:flex-end;padding-bottom:18px;gap:8px;font-size:6px;letter-spacing:.3px;color:var(--text-dark);position:relative}
.feature+.feature::before{content:"";position:absolute;left:0;top:18px;bottom:18px;border-left:1px solid var(--line-light)}
.feature svg{width:32px;height:34px;stroke:var(--text-dark);fill:none;stroke-width:1.3}
.strip{position:absolute;top:301px;left:0;right:0;height:38px;border-top:1px solid var(--line-dark);border-bottom:1px solid var(--line-dark);background:rgba(255,255,255,.03);display:flex;align-items:center;justify-content:center;gap:20px}
.strip__item{display:flex;align-items:center;gap:6px;font-size:6.3px;letter-spacing:.4px;color:var(--text-dim)}
.strip__item svg{width:9px;height:10px;stroke:var(--text-dim);fill:none;stroke-width:1.2}

/* form */
.form-title{font-family:'Cinzel',serif;font-size:12.5px;letter-spacing:.6px}
.rule{position:absolute;left:50%;width:22px;margin-left:-11px;border-top:1px solid}
.form-intro{font-size:7.3px}
.label{position:absolute;left:107px;font-size:6.5px;letter-spacing:.3px;color:var(--text-dark);font-weight:500}
.field{position:absolute;left:107px;width:297px;border:1px solid var(--line-light);border-radius:2px;display:flex;align-items:center;gap:10px;padding-left:10px;font-size:7.3px;color:#9b9b9b;background:var(--paper)}
.field--area{align-items:flex-start;padding-top:9px}
.field svg,.line-field svg{width:10px;height:10px;stroke:#6a6a6a;fill:none;stroke-width:1.2;flex:none}
.btn-solid{position:absolute;display:flex;align-items:center;justify-content:center;font-size:9.5px;letter-spacing:1.5px;border-radius:2px}
.line-field{position:absolute;left:110px;width:292px;border-bottom:1px solid #3a3a3a;display:flex;align-items:flex-start;gap:12px;padding-left:4px;font-size:7px;color:#bdbdbd}
.line-field svg{stroke:#8a8a8a}
.footer{position:absolute;left:0;right:0;bottom:0;height:75px;background:var(--ink);text-align:center;color:var(--text-light);font-size:7.3px;line-height:13.5px;padding-top:30px}
.footer__mark{position:absolute;left:50%;top:11px;width:10px;height:10px;margin-left:-5px;background:var(--text-light)}
</style>
</head>
<body>

<!-- Light variant -->
<section class="page page--light">
  <header class="hero">
    <div class="abs brand" style="top:78px">
      <div class="brand__name"><span class="brand__mark"></span>MARLOW CREST</div>
      <div class="brand__sub">ADVISORY SERVICES</div>
    </div>
    <p class="abs hero__tag" style="top:170px">EXPERT WITNESS &amp; MEDICAL INTEGRATION SERVICES</p>
    <a class="btn-outline" style="left:167px;top:201px;width:180px;height:29px">REQUEST CONSULTATION</a>
  </header>

  <div class="features">
    <div class="feature">
      <svg viewBox="0 0 32 34"><path d="M16 2 L28 6 V16 C28 24 22 29 16 32 C10 29 4 24 4 16 V6 Z"/><path d="M16 10 V25 M10 13 H22 M10 13 L7 19 H13 Z M22 13 L19 19 H25 Z M12 25 H20"/></svg>
      LITIGATION SUPPORT
    </div>
    <div class="feature">
      <svg viewBox="0 0 32 34"><path d="M13 4 H19 V12 H27 V18 H19 V30 H13 V18 H5 V12 H13 Z"/></svg>
      MEDICAL EXPERTS
    </div>
    <div class="feature">
      <svg viewBox="0 0 32 34"><path d="M16 31 C10 23 7 18 7 13 A9 9 0 0 1 25 13 C25 18 22 23 16 31 Z"/><circle cx="16" cy="13" r="3.5"/></svg>
      NATIONWIDE COVERAGE
    </div>
    <div class="feature">
      <svg viewBox="0 0 32 34"><path d="M10 14 V9 A6 6 0 0 1 22 9 V14"/><rect x="6" y="14" width="20" height="17" rx="2"/><circle cx="16" cy="21" r="2"/><path d="M16 23 V26"/></svg>
      CONFIDENTIAL ENGAGEMENT
    </div>
  </div>

  <h2 class="abs form-title" style="top:361px;color:var(--text-dark);font-weight:400">CONNECT WITH ONE OF OUR LIAISONS</h2>
  <span class="rule" style="top:386px;border-color:var(--text-dark)"></span>
  <p class="abs form-intro" style="top:397px;color:#555">Provide your information below and a liaison will be in touch.</p>

  <span class="label" style="top:422px">FULL NAME</span>
  <div class="field" style="top:435px;height:26px"><svg viewBox="0 0 10 10"><circle cx="5" cy="3" r="2.2"/><path d="M1 9.5 C1 6.5 9 6.5 9 9.5"/></svg>Enter your full name</div>
  <span class="label" style="top:474px">EMAIL ADDRESS</span>
  <div class="field" style="top:487px;height:25px"><svg viewBox="0 0 10 10"><rect x=".8" y="2" width="8.4" height="6"/><path d="M.8 2 L5 5.5 L9.2 2"/></svg>Enter your email address</div>
  <span class="label" style="top:524px">CONTACT NUMBER</span>
  <div class="field" style="top:537px;height:25px"><svg viewBox="0 0 10 10"><path d="M2 1 L4 3 L3 4.5 C4 6 4.5 6.5 5.5 7 L7 6 L9 8 L7.5 9.3 C4.5 9 1 5.5 .7 2.5 Z"/></svg>Enter your contact number</div>
  <span class="label" style="top:574px">DESCRIPTION OF PROJECT</span>
  <div class="field field--area" style="top:587px;height:47px"><svg viewBox="0 0 10 10"><path d="M2 .7 H6 L8 2.7 V9.3 H2 Z M3.5 5 H6.5 M3.5 7 H6.5"/></svg>Provide details about your project</div>

  <a class="btn-solid" style="left:107px;top:648px;width:297px;height:29px;background:var(--ink);color:var(--text-light)">SUBMIT CONFIDENTIAL INQUIRY</a>

  <footer class="footer">
    <span class="footer__mark"></span>
    © The Marlow Crest Advisory Services<br>All inquiries are handled with strict confidentiality.
  </footer>
</section>

<!-- Dark variant -->
<section class="page page--dark">
  <div class="abs brand" style="top:110px">
    <div class="brand__name"><span class="brand__mark"></span>MARLOW CREST</div>
    <div class="brand__sub">ADVISORY SERVICES</div>
  </div>
  <p class="abs hero__tag" style="top:202px;color:#bcbcbc">EXPERT WITNESS &amp; MEDICAL INTEGRATION SERVICES</p>
  <a class="btn-outline" style="left:176px;top:230px;width:162px;height:31px">REQUEST CONSULTATION</a>

  <div class="strip">
    <span class="strip__item"><svg viewBox="0 0 9 10"><path d="M4.5 .6 L8.3 1.8 V5 C8.3 7.3 6.5 8.7 4.5 9.5 C2.5 8.7 .7 7.3 .7 5 V1.8 Z M3 5 L4.2 6.2 L6.2 3.8"/></svg>LITIGATION SUPPORT</span>
    <span class="strip__item"><svg viewBox="0 0 9 10"><path d="M4.5 .6 L8.3 1.8 V5 C8.3 7.3 6.5 8.7 4.5 9.5 C2.5 8.7 .7 7.3 .7 5 V1.8 Z M3 5 L4.2 6.2 L6.2 3.8"/></svg>MEDICAL EXPERTS</span>
    <span class="strip__item"><svg viewBox="0 0 9 10"><path d="M4.5 .6 L8.3 1.8 V5 C8.3 7.3 6.5 8.7 4.5 9.5 C2.5 8.7 .7 7.3 .7 5 V1.8 Z M3 5 L4.2 6.2 L6.2 3.8"/></svg>NATIONWIDE COVERAGE</span>
    <span class="strip__item"><svg viewBox="0 0 9 10"><path d="M4.5 .6 L8.3 1.8 V5 C8.3 7.3 6.5 8.7 4.5 9.5 C2.5 8.7 .7 7.3 .7 5 V1.8 Z M3 5 L4.2 6.2 L6.2 3.8"/></svg>CONFIDENTIAL ENGAGEMENT</span>
  </div>

  <h2 class="abs form-title" style="top:370px;color:var(--text-light);font-weight:400">CONNECT WITH ONE OF OUR LIAISONS</h2>
  <span class="rule" style="top:395px;border-color:#777"></span>
  <p class="abs form-intro" style="top:408px;color:var(--text-dim)">Provide your information below and a liaison will be in touch.</p>

  <div class="line-field" style="top:436px;height:19px"><svg viewBox="0 0 10 10"><circle cx="5" cy="3" r="2.2"/><path d="M1 9.5 C1 6.5 9 6.5 9 9.5"/></svg>Full Name</div>
  <div class="line-field" style="top:475px;height:19px"><svg viewBox="0 0 10 10"><rect x=".8" y="2" width="8.4" height="6"/><path d="M.8 2 L5 5.5 L9.2 2"/></svg>Email Address</div>
  <div class="line-field" style="top:514px;height:19px"><svg viewBox="0 0 10 10"><path d="M2 1 L4 3 L3 4.5 C4 6 4.5 6.5 5.5 7 L7 6 L9 8 L7.5 9.3 C4.5 9 1 5.5 .7 2.5 Z"/></svg>Contact Number</div>
  <div class="line-field" style="top:549px;height:41px"><svg viewBox="0 0 10 10"><path d="M2 .7 H6 L8 2.7 V9.3 H2 Z M3.5 5 H6.5 M3.5 7 H6.5"/></svg>Description of Project</div>

  <a class="btn-solid" style="left:150px;top:609px;width:208px;height:28px;background:var(--button-light);color:var(--ink)">SUBMIT CONFIDENTIAL INQUIRY</a>

  <footer class="footer" style="background:transparent;border-top:1px solid var(--line-dark);height:100px;padding-top:45px;color:#bdbdbd">
    <span class="footer__mark" style="top:19px;background:#bdbdbd"></span>
    © The Marlow Crest Advisory Services<br>All inquiries are handled with strict confidentiality.
  </footer>
</section>

</body>
</html>
```